Wine Label Design for the red wine named “Amber Moth Ridge” or “A/M”

Create an elegant yet simple (less is more) label for a red, full-bodied wine from a family-owned Herzegovinian vineyard by the river with 9 names. You can use elements such as the Calopteryx virgo, possibly the river shape, and ensure a coherent storytelling of the unique vineyard’s locality and meticulous, hand-picked grape cultivation.
Let’s craft a label that is not just seen, but is experienced and remembered.

Target Market(s)

Wine lovers that appreciate high quality wines

Industry/Entity Type

Wine, Family owned small producer

Requirements
Must have
• Name A/M, front and back label. Premium feel, uniqueness. Simple but interesting.
Nice to have
• Please see the images below as an idea of various directions. I am also leaning to embossed image on the label
Should not have
• Should not be overcrowded with text, too many images and objects

```html
<!DOCTYPE html>
<html lang="en">
<head>
<meta charset="utf-8">
<title>Amber Moth Ridge — Wine Label</title>
<link rel="stylesheet" href="https://fonts.googleapis.com/css2?family=Oswald:wght@500;600&display=swap">
<style>
  :root {
    --paper: #ffffff;
    --sky: #e0c0a4;
    --sun: #d9af70;
    --ridge-ochre: #a4704f;
    --ridge-plum: #7b5352;
    --ridge-red: #a44f4c;
    --forest: #50705f;
    --sage: #66927f;
    --sand: #f0e6cc;
    --label-ink: #ffffff;
  }
  * { margin: 0; padding: 0; box-sizing: border-box; }
  html, body {
    width: 1200px;
    height: 1029px;
    overflow: hidden;
    background: var(--paper);
  }
  .canvas {
    position: relative;
    width: 1200px;
    height: 1029px;
    background: var(--paper);
  }
  .label {
    position: absolute;
    left: 387px;
    top: 134px;
    width: 426px;
    height: 760px;
  }
  .label__art {
    position: absolute;
    inset: 0;
    width: 100%;
    height: 100%;
  }
  .label__title {
    position: absolute;
    left: 0;
    right: 0;
    top: 190px;
    display: flex;
    flex-direction: column;
    align-items: center;
    font-family: "Oswald", "Arial Narrow", sans-serif;
    font-weight: 600;
    color: var(--label-ink);
    text-transform: uppercase;
    line-height: 1;
  }
  .label__line--major { font-size: 72px; letter-spacing: 2px; }
  .label__line--minor { font-size: 54px; font-weight: 500; letter-spacing: 4px; margin: 6px 0; }
  .label__initials {
    font-size: 40px;
    font-weight: 500;
    letter-spacing: 6px;
    margin-top: 28px;
  }
</style>
</head>
<body>
  <main class="canvas">
    <section class="label">
      <svg class="label__art" viewBox="0 0 485 866" preserveAspectRatio="none"
           role="img" aria-label="Layered landscape illustration: sunset over amber and red mountain ridges, green hills and a winding river valley, inside a hexagon">
        <defs>
          <linearGradient id="landscape" x1="0" y1="0" x2="0" y2="1">
            <stop offset="0" stop-color="var(--sky)"/>
            <stop offset="0.14" stop-color="var(--sun)"/>
            <stop offset="0.26" stop-color="var(--ridge-ochre)"/>
            <stop offset="0.40" stop-color="var(--ridge-plum)"/>
            <stop offset="0.52" stop-color="var(--ridge-red)"/>
            <stop offset="0.64" stop-color="var(--forest)"/>
            <stop offset="0.76" stop-color="var(--sage)"/>
            <stop offset="0.84" stop-color="var(--sand)"/>
            <stop offset="1" stop-color="var(--sand)"/>
          </linearGradient>
        </defs>
        <polygon points="241,0 483,138 483,718 237,866 0,730 5,136" fill="url(#landscape)"/>
      </svg>
      <h1 class="label__title">
        <span class="label__line--major">Amber</span>
        <span class="label__line--minor">Moth</span>
        <span class="label__line--major">Ridge</span>
        <span class="label__initials">A/M</span>
      </h1>
    </section>
  </main>
</body>
</html>
```